Business card design needed

see my website

www.aldermoorandpike.com

I am after a new logo and business card needs to fit in with the website. I like the look of typewriter text - would like this on the website as well if I could!

Industry/Entity Type

Business

Contact Information for Business Card

Aldermoor and Pike
Design and Heritage Consultants

Marisa Oakton
Principal

+61 407 963 215
marisa@aldermoorandpike.com

www.aldermoorandpike.com

back of card

Interior Design
Consultancy on Period Home restoration and renovation
Heritage Impact Statements
Conservation Management Plans
Materials Conservation
Historical Research

```html
<!DOCTYPE html>
<html lang="en">
<head>
<meta charset="utf-8">
<title>Aldermoor and Pike — Business Card</title>
<link rel="stylesheet" href="https://fonts.googleapis.com/css2?family=Special+Elite&family=Courier+Prime:wght@400;700&display=swap">
<style>
  :root {
    --backdrop: #1f1f20;
    --card-grey: #464646;
    --teal: #1fa894;
    --ink: #3a3834;
    --paper-white: #f2f0ec;
    --photo-light: #e4dfd6;
    --photo-mid: #c9bfae;
    --photo-dark: #a79a85;
  }
  * { box-sizing: border-box; margin: 0; padding: 0; }
  html, body {
    width: 1200px; height: 900px; overflow: hidden;
    background: var(--backdrop);
  }
  .stage {
    position: relative; width: 1200px; height: 900px;
    display: flex; flex-direction: column; align-items: center; justify-content: center;
    gap: 48px;
  }
  .card {
    position: relative; width: 630px; height: 360px;
    overflow: hidden;
    box-shadow: 0 10px 28px rgba(0,0,0,.5);
  }
  .text-font {
    font-family: "Courier Prime", "Courier New", monospace;
  }
  .brand-name {
    font-family: "Courier Prime", "Courier New", monospace;
    font-weight: 400;
    line-height: 1.1;
  }
  .brand-tagline {
    font-family: "Courier Prime", "Courier New", monospace;
    font-weight: 400;
    line-height: 1.25;
  }

  /* Services side */
  .card--services .interior-photo {
    position: absolute; inset: 0;
    background:
      linear-gradient(90deg, rgba(255,255,255,.55), rgba(255,255,255,.35)),
      linear-gradient(120deg, var(--photo-light) 0%, var(--photo-mid) 45%, var(--photo-dark) 100%);
  }
  .card--services .content {
    position: absolute; left: 58px; top: 70px; right: 40px;
  }
  .card--services .brand-name { font-size: 36px; color: var(--ink); }
  .card--services .brand-tagline { font-size: 19px; color: var(--ink); margin-top: 8px; }
  .service-list {
    list-style: none; margin-top: 30px;
    font-family: "Courier Prime", "Courier New", monospace;
    font-size: 14px; line-height: 1.35; color: var(--ink);
  }
  .service-list li + li { margin-top: 14px; }
  .sep { color: var(--teal); padding: 0 4px; }

  /* Contact side */
  .card--contact { background: var(--card-grey); }
  .card--contact .person {
    position: absolute; left: 56px; top: 52px;
  }
  .person-name {
    font-family: "Special Elite", "Courier New", monospace;
    font-size: 31px; color: var(--teal); line-height: 1;
  }
  .person-role {
    font-family: "Courier Prime", "Courier New", monospace;
    font-size: 19px; color: var(--paper-white); margin-top: 4px;
  }
  .contact-list {
    list-style: none; margin-top: 22px;
    font-family: "Courier Prime", "Courier New", monospace;
    font-size: 18px; line-height: 1.3; color: var(--paper-white);
  }
  .contact-label { color: var(--teal); margin-right: 8px; }
  .card--contact .brand {
    position: absolute; left: 56px; bottom: 44px;
  }
  .card--contact .brand-name { font-size: 30px; color: var(--paper-white); }
  .card--contact .brand-tagline { font-size: 17px; color: var(--paper-white); margin-top: 4px; }
</style>
</head>
<body>
<main class="stage">

  <section class="card card--services">
    <div class="interior-photo" role="img" aria-label="Softly faded photograph of a period home interior under restoration, with timber doors and stairs"></div>
    <div class="content">
      <h1 class="brand-name">Aldermoor and Pike</h1>
      <p class="brand-tagline">Design and Heritage Consultants</p>
      <ul class="service-list">
        <li>Interior Design Consultancy on Period Home restoration<br>and renovation Heritage</li>
        <li>Impact Statements<span class="sep">/</span>Conservation Management Plans<br>Materials Conservation<span class="sep">/</span>Historical Research.</li>
      </ul>
    </div>
  </section>

  <section class="card card--contact">
    <div class="person">
      <h2 class="person-name">Marisa Oakton</h2>
      <p class="person-role">Principal</p>
      <ul class="contact-list">
        <li><span class="contact-label">P:</span>+61 407 963 215</li>
        <li><span class="contact-label">E:</span>marisa@aldermoorandpike.com</li>
        <li><span class="contact-label">W:</span>www.aldermoorandpike.com</li>
      </ul>
    </div>
    <div class="brand">
      <p class="brand-name">Aldermoor and Pike</p>
      <p class="brand-tagline">Design and Heritage Consultants</p>
    </div>
  </section>

</main>
</body>
</html>
```